opening page for professional healing and psychology program

wordpress opening page that can be inserted in already existing design for the back end, but with a new look for the splash page. Our company is about consciousness, being grounded and doing good work in the world, learning energy healing and depth psychology - not interested in the typical lotus flowers or chakras etc. I have included design elements I am interested in working with and would love your help making it all work together. The side bar, listed below as "old brightfern splash page" (to see it as it is online now, brightferncollege.example) on the right MUST BE INCLUDED on the page, but can be reformatted to work with new design. I am interested in bright colors and a sense of aliveness. There is a video for the page, youtube link included https://videohost.example/v/Qm7xTrpL2ka
Updates

In the bottom three boxes for the page, I need to replace the BLOG section with this photo andTHE ORIGINAL ONGOING HEALERS'FORUMDeborah Allen and Ray Quillen and photo I am trying to load into the brief called m and r africa Added Saturday, April 22, 2017

Target Market(s)

mid-life professionals in the healing arts including acupuncturists, nurses, doctors, therapists, hands on energy workers, etc.

Industry/Entity Type

Health And Wellness

Colors

Designer to choose colors to be used in the design.

Requirements
Must have
• Originality, color, and welcome
Nice to have
• dynamic alive design that draws you in to growth and change and curiosity
• integrate with colors in logo
Should not have
• chakras, lotus flowers, typical mediation site stuff

```html
<!DOCTYPE html>
<html lang="en">
<head>
<meta charset="utf-8">
<title>Brightfern Institute</title>
<link href="https://fonts.googleapis.com/css2?family=Open+Sans:wght@400;600;700&family=Raleway:wght@300;400;500&display=swap" rel="stylesheet">
<style>
:root{
  --navy:#2d3451;
  --navy-dark:#22283f;
  --ink:#333;
  --muted:#666;
  --grey-bg:#efefef;
  --card-bg:#ececec;
  --line:#cfcfcf;
  --black:#111;
  --white:#fff;
  --accent:#f2a31b;
}
*{box-sizing:border-box;margin:0;padding:0}
html,body{width:1200px;height:3468px;overflow:hidden}
body{font-family:"Open Sans",Arial,sans-serif;color:var(--ink);background:var(--white);position:relative}
.abs{position:absolute}
.heading{font-family:"Raleway",Arial,sans-serif;font-weight:400;color:#222;text-align:center}
.divider{display:flex;align-items:center;justify-content:center;gap:14px}
.divider span{display:block;width:200px;height:1px;background:var(--line)}
.divider i{display:block;width:20px;height:20px;border:2px solid #888;border-radius:50%}
.btn{background:var(--navy);color:var(--white);font-weight:600;display:inline-flex;align-items:center;justify-content:center}

/* header */
.header{top:0;left:0;width:1200px;height:111px;background:var(--white)}
.brand{display:flex;align-items:center;gap:12px;font-family:"Raleway",Arial,sans-serif;font-weight:500;color:var(--navy);font-size:28px;line-height:1}
.brand b{display:block;width:54px;height:54px;border-radius:50%;background:var(--navy);flex:none}
.partner{left:450px;top:14px;font-family:"Raleway",Arial,sans-serif;font-weight:500;font-size:24px;color:var(--accent);display:flex;align-items:center;gap:10px}
.partner b{width:28px;height:28px;border-radius:50%;background:var(--accent);display:block}
.contact-top{top:20px;left:705px;font-size:13px;color:#555;display:flex;gap:36px}
.nav{left:405px;top:69px;width:795px;height:42px;background:var(--navy);display:flex;align-items:center;justify-content:space-around;padding-left:40px}
.nav a{color:var(--white);font-size:14px;text-decoration:none;font-weight:600}
.nav a.active{background:#3d4566;padding:12px 18px}

/* hero */
.hero{top:111px;left:0;width:1200px;height:541px;background:linear-gradient(180deg,#b9d3e6 0%,#8fb1c9 45%,#6d7f88 75%,#7a6a58 100%)}
.hero-text{left:99px;top:258px;color:var(--white);font-size:24px;font-weight:700;line-height:1.45;width:600px;text-shadow:0 1px 2px rgba(0,0,0,.25)}
.hero-btns{left:99px;top:474px;display:flex;gap:14px}
.hero-btns .btn{height:44px;padding:0 26px;font-size:18px}

/* we are */
.we-are-title{top:695px;left:0;width:1200px;font-size:38px}
.we-are-div{top:750px;left:0;width:1200px}
.we-are-text{top:790px;left:130px;width:940px;text-align:center;font-size:14px;line-height:1.6;color:#444}
.tablet{top:858px;left:312px;width:578px;height:400px;background:#1d1d1d;border-radius:34px;padding:28px 34px}
.tablet .screen{width:100%;height:100%;background:linear-gradient(135deg,#e8e2d8,#b59a86 60%,#6b5a52)}

/* what we do */
.together{top:1288px;left:0;width:1200px;height:573px;background:var(--grey-bg);overflow:hidden}
.together-title{top:50px;left:0;width:1200px;font-size:38px}
.together-div{top:104px;left:0;width:1200px}
.label{font-size:14px;line-height:1.45;color:#333;width:250px}
.arc-logo{left:440px;top:420px;width:320px;justify-content:center}

/* cards */
.card{top:1914px;height:236px;width:484px;background:var(--card-bg);display:flex}
.card .photo{width:248px;height:236px}
.card .body{padding:30px 16px 0 16px;flex:1}
.card h3{font-size:16px;font-weight:600;color:#222;margin-bottom:12px;text-transform:uppercase}
.card p{font-size:12px;line-height:1.6;color:#555}
.card .btn{margin-top:14px;height:30px;padding:0 16px;font-size:13px}

/* videos */
.videos{top:2203px;left:0;width:1200px;height:451px;background:linear-gradient(180deg,#3a4154,#2a3040 60%,#4a4e5a)}
.videos-title{top:45px;left:0;width:1200px;font-size:38px;color:var(--white)}
.videos-div{top:98px;left:0;width:1200px}
.videos-div span{background:#7a8096}
.videos-div i{border-color:#bbb}
.thumb{top:151px;width:316px;height:171px;border:4px solid var(--white)}
.thumb svg{position:absolute;left:50%;top:50%;transform:translate(-50%,-50%)}
.quote{top:340px;width:316px;text-align:center;color:var(--white);font-size:13px;line-height:1.55}
.slide-arrow{top:225px}

/* events & blog */
.section-title{font-family:"Raleway",Arial,sans-serif;font-size:28px;color:#222;text-transform:uppercase}
.date{width:58px;background:var(--navy);color:var(--white);text-align:center;font-weight:700;line-height:1.15;padding-top:8px}
.date .d{font-size:18px}.date .m{font-size:12px}.date .y{font-size:13px}
.event h4{font-size:16px;font-weight:600;color:#222;margin-bottom:8px}
.event p{font-size:12px;line-height:1.6;color:#555}

/* newsletter */
.newsletter{top:3052px;left:0;width:1200px;height:85px;background:var(--navy);color:var(--white)}
.newsletter .title{left:160px;top:22px;font-family:"Raleway",Arial,sans-serif;font-size:30px}
.newsletter .field{left:430px;top:25px;width:500px;height:38px;background:var(--white);color:#999;font-size:12px;padding:11px 12px}
.newsletter .btn{left:952px;top:25px;width:146px;height:38px;background:var(--navy-dark);font-size:16px}

/* footer */
.footer{top:3137px;left:0;width:1200px;height:291px;background:var(--black);color:var(--white)}
.footer h5{font-size:17px;font-weight:600;text-transform:uppercase;padding-bottom:12px;border-bottom:1px solid #444;margin-bottom:14px}
.footer ul{list-style:none;font-size:13px;line-height:2.6}
.footer ul li:before{content:"• "}
.input{background:#444;color:#ccc;font-size:11px;height:26px;padding:6px 10px;margin-bottom:8px;width:235px}
.copyright{top:3428px;left:0;width:1200px;height:40px;background:#0c0c0c;color:#ccc;font-size:12px;text-align:center;line-height:40px}
</style>
</head>
<body>

<header class="abs header">
  <div class="abs brand" style="left:99px;top:26px"><b></b>Brightfern Institute</div>
  <div class="abs partner"><b></b>Menders' Circle</div>
  <div class="abs contact-top"><span>☎ (555) 014-2290</span><span>✉ Officemanager@BrightfernCollege.example</span></div>
  <nav class="abs nav">
    <a class="active">HOME</a><a>ABOUT US ⌄</a><a>WHAT WE OFFER ⌄</a><a>SHOP</a><a>CONTACT US</a>
  </nav>
</header>

<section class="abs hero" role="img" aria-label="Hiker resting on a mountain rock above a hazy valley">
</section>
<p class="abs hero-text">in the summer of 2017, The Brightfern Institute transitioned to the care of Senior Faculty Marion Tesky and the Menders' Circle.<br>Please continue to travel with us on this new part of the journey.</p>
<div class="abs hero-btns"><span class="btn">Class Registration</span><span class="btn">Sign Up For Newsletter</span></div>

<h2 class="abs heading we-are-title">WE ARE</h2>
<div class="abs divider we-are-div"><span></span><i></i><span></span></div>
<p class="abs we-are-text">A program for lifelong learners in consciousness, healing, energy work, and depth psychology A place to grow with a community of people working to create or enhance careers in the healing arts Committed to resilience, commitment, support and love</p>
<div class="abs tablet"><div class="screen" role="img" aria-label="Introductory video of a faculty member speaking"></div></div>

<section class="abs together">
  <h2 class="abs heading together-title">WHAT WE DO TOGETHER</h2>
  <div class="abs divider together-div"><span></span><i></i><span></span></div>
  <svg class="abs" style="left:0;top:0" width="1200" height="573" viewBox="0 0 1200 573">
    <circle cx="601" cy="565" r="300" fill="none" stroke="#2d3451" stroke-width="18"/>
    <circle cx="601" cy="565" r="268" fill="none" stroke="#2d3451" stroke-width="2"/>
    <g fill="#2d3451" stroke="#fff" stroke-width="4">
      <circle cx="601" cy="245" r="44"/>
      <circle cx="423" cy="314" r="42"/>
      <circle cx="779" cy="314" r="42"/>
      <circle cx="331" cy="464" r="42"/>
      <circle cx="862" cy="464" r="42"/>
    </g>
    <g fill="none" stroke="#fff" stroke-width="3" stroke-linecap="round">
      <rect x="587" y="225" width="28" height="40" rx="3"/><circle cx="601" cy="236" r="4"/><path d="M594 248h14M601 244v14"/>
      <circle cx="430" cy="298" r="4"/><path d="M428 305l-6 12 8 6M422 317l-10 8M428 305l12 4M410 304h-8M412 312h-10"/>
      <circle cx="779" cy="298" r="5"/><path d="M779 305v12M766 328h26M770 322l9-5 9 5"/>
      <path d="M320 446c14-6 28 2 28 16 0 8-5 12-5 18h-14v-6c-8 0-12-4-12-10"/><circle cx="334" cy="462" r="4"/>
      <circle cx="862" cy="464" r="18"/><path d="M862 454v10l7 5"/>
    </g>
  </svg>
  <p class="abs label" style="left:476px;top:148px;text-align:center">Enjoy better health and vitality for yourself and give that gift to others</p>
  <p class="abs label" style="left:125px;top:285px;text-align:right">Improve and deepen your relationships by understanding hidden truths</p>
  <p class="abs label" style="left:836px;top:285px;width:220px">Cultivate your natural healing abilities with a supportive community</p>
  <p class="abs label" style="left:30px;top:432px;text-align:right">Develop the skills needed to successfully facilitate healing for yourself and others</p>
  <p class="abs label" style="left:918px;top:432px;width:230px">Make a living doing what you love without draining yourself or your bank account</p>
  <div class="abs brand arc-logo"><b></b>Brightfern Institute</div>
</section>

<article class="abs card" style="left:99px">
  <div class="photo" style="background:linear-gradient(135deg,#d8c7a6,#8f7a5a)" role="img" aria-label="Two faculty members standing outdoors"></div>
  <div class="body"><h3>About Us</h3><p>Lorem Ipsum is simply dummy text of the printing and typesetting industry. Lorem Ipsum has been the industry's standard dummy text ever since the 1500s, when an unknown printer...</p><span class="btn">Read More</span></div>
</article>
<article class="abs card" style="left:615px">
  <div class="photo" style="background:linear-gradient(180deg,#6f8fb0,#3f5878)" role="img" aria-label="Program artwork of a globe with wings and roots"></div>
  <div class="body"><h3>Steady Ground -<br>Open Sky</h3><p>Lorem Ipsum is simply dummy text of the printing and typesetting industry. Lorem Ipsum has been the industry's standard dummy text ever since...</p><span class="btn">Read More</span></div>
</article>

<section class="abs videos">
  <h2 class="abs heading videos-title">OUR VIDEOS</h2>
  <div class="abs divider videos-div"><span></span><i></i><span></span></div>
  <svg class="abs slide-arrow" style="left:55px" width="24" height="44"><path d="M20 2L4 22l16 20" fill="none" stroke="#ccc" stroke-width="2"/></svg>
  <svg class="abs slide-arrow" style="left:1120px" width="24" height="44"><path d="M4 2l16 20L4 42" fill="none" stroke="#ccc" stroke-width="2"/></svg>
  <div class="abs thumb" style="left:99px;background:linear-gradient(135deg,#e8dcc6,#b59a78)" role="img" aria-label="Student testimonial video">
    <svg width="48" height="48"><circle cx="24" cy="24" r="22" fill="rgba(45,52,81,.85)" stroke="#fff" stroke-width="2"/><path d="M19 14l14 10-14 10z" fill="#fff"/></svg></div>
  <div class="abs thumb" style="left:442px;background:linear-gradient(135deg,#4a4032,#1e1a16)" role="img" aria-label="Student testimonial video">
    <svg width="48" height="48"><circle cx="24" cy="24" r="22" fill="rgba(45,52,81,.85)" stroke="#fff" stroke-width="2"/><path d="M19 14l14 10-14 10z" fill="#fff"/></svg></div>
  <div class="abs thumb" style="left:786px;background:linear-gradient(135deg,#e2d2b4,#a0866a)" role="img" aria-label="Student testimonial video">
    <svg width="48" height="48"><circle cx="24" cy="24" r="22" fill="rgba(45,52,81,.85)" stroke="#fff" stroke-width="2"/><path d="M19 14l14 10-14 10z" fill="#fff"/></svg></div>
  <p class="abs quote" style="left:99px">"I feel incredibly blessed and honored to be here. I came intending to open my heart and that's what happened!"</p>
  <p class="abs quote" style="left:442px">"Before I went to Brightfern, I struggled with getting pregnant, it wasn't happening..."</p>
  <p class="abs quote" style="left:786px">"A friend said, 'People don't change.' But I was able to communicate to him, people do change. I've changed, because of this."</p>
</section>

<h2 class="abs section-title" style="left:99px;top:2700px">Upcoming Brightfern Events</h2>
<div class="abs" style="left:99px;top:2750px;width:467px;height:1px;background:var(--line)"></div>
<div class="abs" style="left:600px;top:2680px;width:1px;height:340px;background:var(--line)"></div>
<div class="abs date" style="left:99px;top:2797px;height:82px"><div class="d">26</div><div class="m">APR</div><div class="y">2017</div></div>
<div class="abs event" style="left:176px;top:2800px;width:390px"><h4>Level 1 Body Mind Balance Certification</h4><p>Lorem Ipsum is simply dummy text of the printing and typesetting industry. Lorem Ipsum has been the industry's standard...[+]</p></div>
<div class="abs date" style="left:99px;top:2913px;height:86px"><div class="d">26</div><div class="m">APR</div><div class="y">2017</div></div>
<div class="abs event" style="left:176px;top:2916px;width:390px"><h4>Level 2 Energy Healing Counselor Certification</h4><p>Lorem Ipsum is simply dummy text of the printing and typesetting industry. Lorem Ipsum has been the industry's standard...[+]</p></div>

<h2 class="abs section-title" style="left:636px;top:2700px">Latest Blog</h2>
<svg class="abs" style="left:1058px;top:2712px" width="42" height="18"><circle cx="9" cy="9" r="7" fill="none" stroke="#aaa"/><circle cx="33" cy="9" r="7" fill="none" stroke="#333"/><path d="M31 5l4 4-4 4" fill="none" stroke="#333"/></svg>
<div class="abs" style="left:636px;top:2797px;width:201px;height:202px;border:3px solid #ddd;background:linear-gradient(135deg,#8aa36a,#4f6b3a)" role="img" aria-label="Blog photo of a woman in a yoga pose"></div>
<div class="abs date" style="left:645px;top:2806px;height:76px;background:rgba(45,52,81,.9)"><div class="d">26</div><div class="m">APR</div><div class="y">2017</div></div>
<div class="abs event" style="left:862px;top:2797px;width:238px"><h4>Lorem Ipsum is simply dummy text of the printng typesetting.</h4><p>Lorem Ipsum is simply dummy text of the printing and typesetting industry. Lorem Ipsum has been the industry's standard dummy text ever since the 1500s, when an unknown printer took a galley of type and scrambled it to make a type specimen book...[+]</p></div>

<section class="abs newsletter">
  <svg class="abs" style="left:99px;top:20px" width="46" height="46"><circle cx="23" cy="23" r="22" fill="#fff"/><rect x="11" y="15" width="24" height="16" fill="none" stroke="#2d3451" stroke-width="2"/><path d="M11 15l12 9 12-9" fill="none" stroke="#2d3451" stroke-width="2"/></svg>
  <div class="abs title">Newsletter Signup</div>
  <div class="abs field">Your e-mail Address</div>
  <span class="abs btn">SIGN UP</span>
</section>

<footer class="abs footer">
  <div class="abs" style="left:99px;top:40px;width:140px"><h5>Quick Links</h5><ul><li>Home</li><li>About Us</li><li>What We Offer</li><li>Shop</li><li>Contact Us</li></ul></div>
  <div class="abs" style="left:270px;top:40px;width:250px"><h5>Quick Inquiry</h5>
    <div class="input">Name</div><div class="input">Email</div><div class="input" style="height:56px">Message</div>
    <span class="btn" style="background:#fff;color:#111;height:28px;width:96px;font-size:12px;margin-top:4px">SUBMIT</span></div>
  <div class="abs" style="left:562px;top:40px;width:320px"><h5>Quick Contact</h5>
    <div style="display:flex;gap:14px;font-size:13px;line-height:1.55;margin-bottom:18px">
      <svg width="22" height="30"><path d="M11 2a8 8 0 0 0-8 8c0 6 8 18 8 18s8-12 8-18a8 8 0 0 0-8-8z" fill="#fff"/><circle cx="11" cy="10" r="3" fill="#111"/></svg>
      <div><b>brightfern institute</b><br>P.O. Box 4410-200, Cedar Vale, CA 90017</div></div>
    <div style="display:flex;gap:14px;font-size:13px;margin-bottom:22px"><svg width="22" height="18"><rect x="1" y="1" width="20" height="16" rx="3" fill="#fff"/><path d="M6 5c0 5 4 9 9 9" stroke="#111" stroke-width="2" fill="none"/></svg>(555) 014-2290 , (555) 014-7781</div>
    <div style="display:flex;gap:14px;font-size:13px"><svg width="22" height="16"><rect x="1" y="1" width="20" height="14" fill="#fff"/><path d="M1 1l10 7 10-7" stroke="#111" fill="none"/></svg>Officemanager@BrightfernCollege.example</div></div>
  <div class="abs brand" style="left:920px;top:135px;color:#fff;font-size:24px"><b style="background:#fff;width:44px;height:44px"></b>Brightfern Institute</div>
</footer>
<div class="abs copyright">Copyright © 2017 brightfern institute. All Rights Reserved.</div>

</body>
</html>
```